web site update

I want to get a better website for a small high end remodeling and construction company
I currently have a web site but you will find that it is not good.
www.quenbrickhall.com
We are a high end construction / remodeling company that has been in business since 2003. We primarily work in the mid peninsula of the bay area. Most of our clientele are very educated captains of industry. This group is still the target client.
I had my logo designed by Mint Easel a few years ago and I do like it, I like the orange and black or orange a blue. I don’t have a lot of content on hand as far as professional photographs.
Number of pages not sure and are open to: design pages vs full function website
I think what I am after is a web presence that will seal the deal as we are getting high referrals from past clients.
Construction
1 page

```html
<!DOCTYPE html>
<html lang="en">
<head>
<meta charset="utf-8">
<title>Quenbrick Hall – High End Construction &amp; Remodeling</title>
<link rel="stylesheet" href="https://fonts.googleapis.com/css2?family=Montserrat:wght@400;500;600&family=Arimo:ital,wght@0,400;0,700;1,400&display=swap">
<style>
  :root {
    --orange: #ff6a00;
    --orange-deep: #e25900;
    --orange-soft: #ffb27d;
    --ink: #111111;
    --text: #555555;
    --muted: #9a9a9a;
    --white: #ffffff;
    --rule: #e4e4e4;
    --charcoal: #2f2f2f;
  }
  * { margin: 0; padding: 0; box-sizing: border-box; }
  html, body { width: 1200px; height: 2273px; overflow: hidden; background: var(--white); }
  body { position: relative; font-family: "Arimo", Arial, sans-serif; color: var(--text); }
  .abs { position: absolute; }
  .heading { font-family: "Montserrat", Arial, sans-serif; font-weight: 400; color: var(--ink); text-transform: uppercase; white-space: nowrap; }
  .accent { color: var(--orange); }

  /* Hero */
  .hero { left: 0; top: 0; width: 1200px; height: 677px;
    background:
      linear-gradient(90deg, rgba(255,255,255,0) 0%, rgba(255,255,255,0) 55%, rgba(255,255,255,.75) 72%, rgba(246,248,250,.9) 100%),
      linear-gradient(180deg,
        #f3f0eb 0%, #ece8e2 30%, #e6dfd6 44%,
        #d8b48f 52%, #cfa47a 62%, #b98d66 70%,
        #4a3c33 74%, #3b302a 77%,
        #e9e3dc 80%, #d7b996 88%, #c8a07a 100%); }
  .brand { left: 0; top: 34px; width: 1200px; display: flex; justify-content: center; align-items: center; gap: 20px; }
  .brand-mark { width: 70px; height: 70px; background: var(--ink); }
  .brand-name { font-family: "Montserrat", Arial, sans-serif; font-weight: 600; font-size: 36px; letter-spacing: 1px; color: var(--orange); }

  /* Navigation */
  .nav { left: 0; top: 677px; width: 1200px; height: 64px; border-bottom: 1px solid var(--rule); background: var(--white); }
  .nav-item { top: 22px; font-family: "Montserrat", Arial, sans-serif; font-size: 15px; color: #222; transform: translateX(-50%); }
  .nav-active { left: 251px; top: 62px; width: 54px; height: 2px; background: #555; }

  /* Welcome */
  .welcome-title { left: 0; top: 790px; width: 1200px; text-align: center; font-size: 38px; }
  .welcome-copy { left: 155px; top: 853px; width: 890px; text-align: center; font-size: 14.2px; line-height: 22.5px; }
  .btn { left: 523px; top: 939px; width: 154px; height: 50px; border-radius: 25px; background: var(--orange); color: var(--white);
    font-family: "Montserrat", Arial, sans-serif; font-size: 16px; text-align: center; line-height: 50px; }

  /* Newsletter */
  .newsletter { left: 0; top: 1042px; width: 1200px; height: 209px;
    background: linear-gradient(180deg, #ff7a14 0%, #ff6a00 60%, #f25f00 100%); }
  .newsletter-title { left: 0; top: 1072px; width: 1200px; text-align: center; font-size: 37px; }
  .field { left: 350px; top: 1153px; width: 440px; height: 54px; border-radius: 27px 0 0 27px; background: var(--white);
    padding-left: 34px; font-size: 14px; line-height: 54px; color: #555; }
  .submit { left: 694px; top: 1153px; width: 154px; height: 54px; border-radius: 27px; background: var(--charcoal); color: var(--white);
    font-family: "Montserrat", Arial, sans-serif; font-weight: 500; font-size: 21px; text-align: center; line-height: 54px; }

  /* Services */
  .service { top: 1251px; width: 600px; height: 334px; }
  .service-construction { left: 0; background: linear-gradient(120deg, #4d4338 0%, #6a5a48 40%, #3c3530 100%); }
  .service-remodel { left: 600px; background: linear-gradient(120deg, #3f3a36 0%, #5a4e44 45%, #2c2826 100%); }
  .service-title { top: 1344px; width: 600px; text-align: center; font-size: 37px; }
  .service-copy { top: 1414px; width: 600px; padding: 0 78px; text-align: center; font-size: 16px; line-height: 23px; color: var(--white); }

  /* Testimonial */
  .clients-title { left: 0; top: 1636px; width: 1200px; text-align: center; font-size: 38px; }
  .avatar { left: 474px; top: 1698px; width: 82px; height: 82px; border-radius: 50%; background: linear-gradient(160deg, #d8cdbf, #9a8a7c); }
  .client-name { left: 580px; top: 1716px; font-family: "Montserrat", Arial, sans-serif; font-size: 17px; color: var(--orange); }
  .client-role { left: 581px; top: 1746px; font-size: 13px; font-style: italic; color: var(--muted); }
  .quote-copy { left: 264px; top: 1808px; width: 672px; text-align: center; font-size: 14.2px; line-height: 27.5px; }
  .quote-mark { font-family: Georgia, "Times New Roman", serif; font-weight: 700; font-size: 70px; line-height: 1; color: var(--orange); }
  .quote-open { left: 222px; top: 1788px; }
  .quote-close { left: 940px; top: 1860px; }
  .dot { top: 1926px; width: 10px; height: 10px; border-radius: 50%; background: var(--orange); }

  /* Footer */
  .footer { left: 0; top: 1991px; width: 1200px; height: 218px; background: var(--orange); }
  .footer-heading { top: 2013px; font-family: "Montserrat", Arial, sans-serif; font-weight: 400; font-size: 17px; color: var(--white); text-transform: uppercase; }
  .footer-text { font-size: 13.5px; line-height: 23px; color: var(--white); }
  .footer-link-dim { color: var(--orange-soft); }
  .icon { left: 78px; width: 26px; height: 22px; }
  .thumb { top: 2054px; width: 104px; height: 103px; }
  .bar { left: 0; top: 2209px; width: 1200px; height: 64px; background: var(--orange-deep); }
  .copyright { left: 80px; top: 2232px; font-family: "Montserrat", Arial, sans-serif; font-weight: 500; font-size: 13px; color: var(--white); }
  .copyright .soft { color: var(--orange-soft); }
  .social { top: 2234px; width: 13px; height: 13px; border-radius: 50%; background: var(--white); opacity: .85; }
</style>
</head>
<body>

<!-- Hero -->
<div class="abs hero" role="img" aria-label="Photograph of a bright white kitchen with a wooden island, dark countertops, orchids and large windows"></div>
<div class="abs brand">
  <span class="brand-mark"></span>
  <span class="brand-name">QUENBRICK HALL</span>
</div>

<!-- Navigation -->
<nav class="abs nav">
  <span class="abs nav-item" style="left:277px">HOME</span>
  <span class="abs nav-item" style="left:386px">ABOUT</span>
  <span class="abs nav-item" style="left:510px">SERVICES</span>
  <span class="abs nav-item" style="left:645px">PROJECTS</span>
  <span class="abs nav-item" style="left:777px">GALLERY</span>
  <span class="abs nav-item" style="left:909px">CONTACT</span>
  <span class="abs nav-active"></span>
</nav>

<!-- Welcome -->
<h1 class="abs heading welcome-title">Welcome to <span class="accent">Quenbrick Hall</span></h1>
<p class="abs welcome-copy">Lorem Ipsum is simply dummy text of the printing and typesetting industry. Lorem Ipsum has been the industry's standard dummy text ever since the 1500s, when an unknown printer took a galley of type and scrambled it to make a type specimen book. It has survived not only five centuries, but also the leap into electronic typesetting, remaining essentially unchanged.</p>
<span class="abs btn">READ MORE</span>

<!-- Newsletter -->
<section class="abs newsletter" role="img" aria-label="Orange tinted photograph of a city skyline with construction cranes"></section>
<h2 class="abs heading newsletter-title" style="color:var(--white)">Newsletter</h2>
<span class="abs field">E-Mail Address</span>
<span class="abs submit">SUBMIT</span>

<!-- Services -->
<div class="abs service service-construction" role="img" aria-label="Darkened photograph of a dining room in a high end home"></div>
<div class="abs service service-remodel" role="img" aria-label="Darkened photograph of a remodeled living room"></div>
<h2 class="abs heading service-title" style="left:0;color:var(--white)">High End Construction</h2>
<p class="abs service-copy" style="left:0">Lorem Ipsum is simply dummy text of the printing and typesetting industry. Lorem Ipsum has been the industry's standard dummy text ever.</p>
<h2 class="abs heading service-title" style="left:600px;color:var(--white)">Remodeling</h2>
<p class="abs service-copy" style="left:600px">Lorem Ipsum is simply dummy text of the printing and typesetting industry. Lorem Ipsum has been the industry's standard dummy text ever.</p>

<!-- Testimonial -->
<h2 class="abs heading clients-title">What <span class="accent">Clients</span> Say About Us</h2>
<div class="abs avatar" role="img" aria-label="Client portrait photograph"></div>
<span class="abs client-name">DANIEL ORWELL</span>
<span class="abs client-role">CEO, Company Name</span>
<span class="abs quote-mark quote-open">&ldquo;</span>
<p class="abs quote-copy">Lorem Ipsum is simply dummy text of the printing and typesetting industry. Lorem Ipsum has been the industry's standard dummy text ever since the 1500s, when an unknown printer took a galley of type and scrambled it to make a type specimen book.</p>
<span class="abs quote-mark quote-close">&rdquo;</span>
<span class="abs dot" style="left:574px"></span>
<span class="abs dot" style="left:595px;opacity:.6"></span>
<span class="abs dot" style="left:616px;opacity:.25"></span>

<!-- Footer -->
<footer class="abs footer"></footer>
<h3 class="abs footer-heading" style="left:80px">Contact Info</h3>
<h3 class="abs footer-heading" style="left:345px">Useful Links</h3>
<h3 class="abs footer-heading" style="left:558px">Gallery</h3>

<svg class="abs icon" style="top:2052px" viewBox="0 0 26 22" fill="none" stroke="#fff" stroke-width="1.8" stroke-linejoin="round">
  <path d="M2 4 L9 1.5 L17 4 L24 1.5 V18 L17 20.5 L9 18 L2 20.5 Z"/><path d="M9 1.5 V18 M17 4 V20.5"/>
</svg>
<p class="abs footer-text" style="left:111px;top:2050px">123 Building Name, Area,<br>City, Country - Zipcode</p>

<svg class="abs icon" style="top:2113px" viewBox="0 0 26 22" fill="none" stroke="#fff" stroke-width="1.8" stroke-linejoin="round">
  <path d="M4 3 L8 2 L11 7 L8.5 9 Q11 14 15 16 L17 13.5 L22 16.5 L21 20 Q11 20 4 11 Q3 7 4 3 Z"/>
</svg>
<p class="abs footer-text" style="left:111px;top:2112px">415.555.0142</p>

<svg class="abs icon" style="top:2151px" viewBox="0 0 26 22" fill="none" stroke="#fff" stroke-width="1.8" stroke-linejoin="round">
  <rect x="2" y="3" width="22" height="16" rx="2"/><path d="M2.5 4 L13 12 L23.5 4"/>
</svg>
<p class="abs footer-text" style="left:111px;top:2150px">hello@quenbrickhall.com</p>

<p class="abs footer-text" style="left:345px;top:2050px">Privacy Policy</p>
<p class="abs footer-text footer-link-dim" style="left:345px;top:2080px">Terms &amp; Conditions</p>
<p class="abs footer-text footer-link-dim" style="left:345px;top:2112px">Disclaimer</p>

<div class="abs thumb" style="left:556px;background:linear-gradient(150deg,#8d7a66,#4b4038)" role="img" aria-label="Project photo: attic room with window"></div>
<div class="abs thumb" style="left:670px;background:linear-gradient(150deg,#b7b1aa,#5b5650)" role="img" aria-label="Project photo: kitchen counter and cabinets"></div>
<div class="abs thumb" style="left:783px;background:linear-gradient(150deg,#c7b79c,#5e4a36)" role="img" aria-label="Project photo: kitchen with island"></div>
<div class="abs thumb" style="left:898px;background:linear-gradient(150deg,#9a5b35,#3d2618)" role="img" aria-label="Project photo: wooden kitchen with stove"></div>
<div class="abs thumb" style="left:1013px;background:linear-gradient(150deg,#e7ddd2,#9c4a32)" role="img" aria-label="Project photo: bright living room"></div>

<div class="abs bar"></div>
<p class="abs copyright">&copy; <span class="soft">QUENBRICK HALL</span> 2016. All Rights Reserved</p>
<span class="abs social" style="left:1010px"></span>
<span class="abs social" style="left:1040px"></span>
<span class="abs social" style="left:1074px"></span>
<span class="abs social" style="left:1108px"></span>

</body>
</html>
```